KTR-OB R-Value Adjustment Paper

This is a technical paper needing professional layout that is compatible with our current style guidelines; it will be used in digital and print media. It has numerous tables and graphs.

We have attached a report "KTR Cladding EPD" issued to our company under Marrowfield Assurance graphic design guidelines. While this does NOT reflect our style branding, it does represent the 'technical' presentation we are looking for.

To view our typical company design/style please see our website at www.ktrcouncil.org. Our primary RGB colors are: (187,140,9); (94,47,29); (94,138,164); and (164,167,15). Secondary RGB colors are (249,162,28) and (218,210,208). Our title/header font is DIN Next LT Pro and our copy font is Calibri 10.5 pt. We can deviate from the font specification if beneficial.

The attached file, "KTR-OB Rvalue Adj Factor" is a partial representation of the full document that will need design services. For the concepts we would like to see a cover/title page, a text/copy page and a sample of data graphic treatments.Once we have agreed upon a design concept we will determine full costs to complete the project.

Target Market(s)

Building and construction professionals, architects, building code officials

Font styles to use
Other font styles liked:
• DIN Next LT Pro

Requirements
Must have
• Design elements that help make the information easy to read and use.
Nice to have
• Right amount of white space.

```html
<!DOCTYPE html>
<html lang="en">
<head>
<meta charset="utf-8">
<title>Polystyrene Foam Insulation – Effective R-Values</title>
<link href="https://fonts.googleapis.com/css2?family=Barlow:wght@400;500&display=swap" rel="stylesheet">
<style>
:root{
  --brown:#5e2f1d;
  --grey:#7a7a7a;
  --olive-dark:#6f7410;
  --olive:#a4a70f;
  --ink:#1a1a1a;
  --paper:#ffffff;
}
*{margin:0;padding:0;box-sizing:border-box}
html,body{width:848px;height:1200px;overflow:hidden;background:var(--paper)}
.page{position:relative;width:848px;height:1200px;color:var(--ink);font-family:"Barlow",Arial,sans-serif}
.doc-title{position:absolute;left:28px;top:47px;font-weight:500;color:var(--brown);font-size:19.5px;line-height:26px;letter-spacing:1.5px;text-transform:uppercase;white-space:nowrap}
.doc-title .cap{font-size:25px}
.section-head{position:absolute;left:28px;font-weight:500;color:var(--grey);font-size:20.5px;line-height:24px;letter-spacing:1.6px;text-transform:uppercase}
.rule{position:absolute;left:28px;width:792px;height:9px}
.rule.dark{background:var(--olive-dark)}
.rule.light{background:var(--olive)}
.copy,.findings{position:absolute;left:28px;font-size:15.5px;line-height:23px;letter-spacing:.85px;white-space:nowrap}
.findings{list-style:none}
.findings li{position:relative;padding-left:57px}
.findings li::before{content:"";position:absolute;left:43px;top:18px;width:7px;height:7px;border-radius:50%;background:var(--ink)}
</style>
</head>
<body>
<main class="page">
  <h1 class="doc-title"><span class="cap">P</span>olystyrene foam insulation in long-term<br>building applications – effective R-values</h1>

  <h2 class="section-head" style="top:123px">Executive Summary</h2>
  <div class="rule dark" style="top:170px"></div>

  <p class="copy" style="top:211px">The primary purpose of insulation is to isolate a building’s interior environment from either warm or cold<br>exterior conditions.&nbsp; In many building applications, polystyrene foam insulation is protected from moisture,<br>and the R-values determined under dry laboratory conditions are appropriate.&nbsp; This document provides a<br>methodology that uses short-term, laboratory-determined R-values with adjustment factors to account for<br>the long-term conditions of buildings when a more detailed analysis is desired.&nbsp; The focus is on the insulation<br>or R-value performance of expanded polystyrene (EPS) and extruded polystyrene (XPS) foam products used<br>in long-term building applications.&nbsp; A methodology is presented in which the laboratory-determined R-value<br>is multiplied by three adjustment factors to determine the long-term effective R-value of installed insulation.<br>After considering the impact of temperature, age, and moisture on both EPS and XPS, the following<br>conclusions are drawn:</p>

  <ul class="findings" style="top:468px">
    <li>The R-values for EPS and XPS increase when the mean temperature decreases below 75 oF.&nbsp; At a<br>mean temperature of 40 o F, the R-values for EPS and XPS increase by approximately 10%.</li>
    <li>The R-value for EPS was constant over time, and the R-value for XPS decreased by approximately<br>14% over time.</li>
    <li>The R-values for both EPS and XPS is approximated to decrease by10% due to the absorption of<br>water in below-grade applications.</li>
  </ul>

  <p class="copy" style="top:619px">The magnitudes of the adjustments to the R-values were not extremely large, but the analysis demonstrated<br>that the R-value performance of EPS was preserved better than that of XPS when all factors were considered.<br>The prime contributor to this difference was the loss of R-value by XPS that occurred with age.</p>

  <h2 class="section-head" style="top:724px">Introduction</h2>
  <div class="rule light" style="top:762px"></div>

  <p class="copy" style="top:791px">The primary purpose of insulation it is to isolate a building’s interior environment from either warm or cold<br>exterior conditions, i.e., to keep a building warm when it is cold outside or to keep a building cool when it is<br>extremely hot outside. R-value, or thermal resistance, is a measure of the ability of insulation to resist the<br>flow of heat.&nbsp; The higher the R-value, the greater the resistance to heat flow is. A higher R-value translates<br>into lower heating and cooling costs and reduced pollution.</p>

  <p class="copy" style="top:928px">The primary purpose of insulation is to isolate a building’s interior environment from either warm or cold<br>exterior conditions.&nbsp; In many building applications, polystyrene foam insulation is protected from moisture,<br>and the R-values determined under dry laboratory conditions are appropriate.&nbsp; This document provides a<br>methodology that uses short-term, laboratory-determined R-values with adjustment factors to account for<br>the long-term conditions of buildings when a more detailed analysis is desired.&nbsp; The focus is on the insulation<br>or R-value performance of expanded polystyrene (EPS) and extruded polystyrene (XPS) foam products used<br>in long-term building applications.&nbsp; A methodology is presented in which the laboratory-determined R-value<br>is multiplied by three adjustment factors to determine the long-term effective R-value of installed insulation.<br>After considering the impact of temperature, age, and moisture on both EPS and XPS, the following<br>conclusions are drawn:</p>
</main>
</body>
</html>
```